VintnerLoop Restuarant Postcard

I have a list of restaurant owners that I need to get to take Action on my Website.

The Website is:

http://www.vintnerloop.example

The goal of the Post card will be to mail to Restaurant Owners and encourage them to visit our Website and enter some details about their property on our website.

The Card Must Contain the Text:

Get New Customers From:

www.VintnerLoop.example

admin@vintnerloop.example

555-417-2096

The steps I need recipients of the card to take

1. Visit: www.VintnerLoop.example

2. Find your Restaurant using the Search Box

3. Click on Restaurant

4. Click on “Do You”

5. Enter your Corkage Fee Details!

I have loaded a some files:

I added some Logos, as well as some screenshots of my attempts at the post card.

Industry/Entity Type

Restaurant

```html
<!DOCTYPE html>
<html lang="en">
<head>
<meta charset="utf-8">
<title>VintnerLoop Restaurant Postcard</title>
<link rel="stylesheet" href="https://fonts.googleapis.com/css2?family=Pinyon+Script&family=Cormorant+SC:wght@500&family=Montserrat:ital,wght@0,400;0,500;0,800;1,300;1,400&display=swap">
<style>
  :root {
    --page: #ffffff;
    --stripe-dark: #a6a7aa;
    --stripe-light: #b4b5b8;
    --panel-grey: #d1d2d4;
    --frame-band: #c9c9cb;
    --ink: #1b1b1b;
    --ink-soft: #333333;
    --button-blue: #1a9fe0;
    --button-text: #ffffff;
  }
  html, body {
    margin: 0;
    padding: 0;
    overflow: hidden;
    background: var(--page);
  }
  .canvas {
    position: relative;
    width: 1200px;
    height: 923px;
    overflow: hidden;
    background: var(--page);
    font-family: "Montserrat", sans-serif;
    color: var(--ink);
  }

  /* ---------- Card front ---------- */
  .card-front {
    position: absolute;
    left: 432px;
    top: 0;
    width: 768px;
    height: 590px;
    background: repeating-linear-gradient(90deg,
      var(--stripe-dark) 0 38px,
      var(--stripe-light) 38px 76px);
  }
  .card-front .frame {
    position: absolute;
    inset: 0;
  }
  .headline-script {
    position: absolute;
    font-family: "Pinyon Script", cursive;
    line-height: 1;
    color: var(--ink);
  }
  .headline-attract { left: 120px; top: 104px; font-size: 70px; }
  .headline-with { left: 548px; top: 176px; font-size: 54px; }
  .headline-caps {
    position: absolute;
    left: 180px;
    top: 168px;
    font-family: "Cormorant SC", serif;
    font-weight: 500;
    font-size: 42px;
    line-height: 1;
    letter-spacing: 0.5px;
    text-transform: uppercase;
    color: var(--ink);
  }
  .brand-name {
    position: absolute;
    left: 0;
    width: 768px;
    top: 290px;
    text-align: center;
    font-weight: 400;
    font-size: 72px;
    line-height: 1;
    letter-spacing: 1px;
    color: var(--ink);
  }
  .front-url {
    position: absolute;
    left: 0;
    width: 768px;
    top: 448px;
    text-align: center;
    font-style: italic;
    font-weight: 400;
    font-size: 23px;
    color: var(--ink);
  }
  .front-contact {
    position: absolute;
    left: 0;
    width: 768px;
    top: 486px;
    text-align: center;
    font-style: italic;
    font-weight: 400;
    font-size: 16px;
    color: var(--ink-soft);
  }

  /* ---------- Steps panel ---------- */
  .steps-panel {
    position: absolute;
    left: 0;
    top: 333px;
    width: 384px;
    height: 590px;
    background: var(--panel-grey);
    border-right: 2px solid var(--ink);
    box-shadow: 5px 0 0 var(--page), 7px 0 0 var(--ink);
  }
  .steps-title {
    margin: 24px 0 0;
    text-align: center;
    font-weight: 800;
    font-size: 26.5px;
    line-height: 38px;
    letter-spacing: 0.3px;
    color: var(--ink);
  }
  .step {
    position: absolute;
    left: 18px;
    display: flex;
    align-items: flex-start;
  }
  .step-number {
    width: 46px;
    font-family: "Pinyon Script", cursive;
    font-size: 40px;
    line-height: 30px;
    color: var(--ink);
  }
  .step-text {
    font-style: italic;
    font-weight: 300;
    font-size: 18px;
    line-height: 26px;
    color: var(--ink-soft);
  }
  .step-1 { top: 134px; }
  .step-2 { top: 228px; }
  .step-3 { top: 320px; }
  .step-4 { top: 394px; align-items: center; }
  .step-5 { top: 506px; }
  .action-button {
    position: relative;
    display: inline-block;
    width: 230px;
    height: 50px;
    border-radius: 25px;
    background: var(--button-blue);
    color: var(--button-text);
    font-weight: 500;
    font-size: 19px;
    line-height: 50px;
    text-align: center;
    letter-spacing: -0.2px;
  }
  .pointer {
    position: absolute;
    left: 214px;
    top: 20px;
    width: 38px;
    height: 48px;
  }
</style>
</head>
<body>
<main class="canvas">

  <section class="card-front" aria-label="Postcard front">
    <svg class="frame" width="768" height="590" viewBox="0 0 768 590" aria-hidden="true">
      <path d="M78,110 C70,80 95,58 120,62 C200,70 280,58 330,45 C360,38 375,22 384,20 C393,22 408,38 438,45 C488,58 568,70 648,62 C673,58 698,80 690,110 C700,190 740,260 763,296 C740,332 700,402 690,482 C698,512 673,534 648,530 C568,522 488,534 438,547 C408,554 393,570 384,572 C375,570 360,554 330,547 C280,534 200,522 120,530 C95,534 70,512 78,482 C68,402 28,332 5,296 C28,260 68,190 78,110 Z"
            fill="#ffffff" stroke="var(--frame-band)" stroke-width="16"/>
      <path d="M78,110 C70,80 95,58 120,62 C200,70 280,58 330,45 C360,38 375,22 384,20 C393,22 408,38 438,45 C488,58 568,70 648,62 C673,58 698,80 690,110 C700,190 740,260 763,296 C740,332 700,402 690,482 C698,512 673,534 648,530 C568,522 488,534 438,547 C408,554 393,570 384,572 C375,570 360,554 330,547 C280,534 200,522 120,530 C95,534 70,512 78,482 C68,402 28,332 5,296 C28,260 68,190 78,110 Z"
            fill="none" stroke="var(--ink)" stroke-width="3"/>
    </svg>
    <span class="headline-script headline-attract">Attract</span>
    <span class="headline-caps">New Customers</span>
    <span class="headline-script headline-with">with</span>
    <div class="brand-name">VintnerLoop</div>
    <div class="front-url">www.VintnerLoop.example</div>
    <div class="front-contact">admin@vintnerloop.example &nbsp;·&nbsp; 555-417-2096</div>
  </section>

  <section class="steps-panel" aria-label="How to add your details">
    <h2 class="steps-title">ADDING YOUR DETAILS<br>IS EASY!</h2>

    <div class="step step-1">
      <span class="step-number">1.</span>
      <span class="step-text">Visit: www.VintnerLoop.example</span>
    </div>
    <div class="step step-2">
      <span class="step-number">2.</span>
      <span class="step-text">Find your Restaurant using<br>the Search Box</span>
    </div>
    <div class="step step-3">
      <span class="step-number">3.</span>
      <span class="step-text">Click on your Restaurant</span>
    </div>
    <div class="step step-4">
      <span class="step-number">4.</span>
      <span class="action-button">DO YOU
        <svg class="pointer" viewBox="0 0 38 48" aria-hidden="true">
          <path d="M2,2 L2,38 L11,30 L18,45 L25,42 L18,27 L30,27 Z" fill="#ffffff" stroke="#1b1b1b" stroke-width="2.2" stroke-linejoin="round"/>
        </svg>
      </span>
    </div>
    <div class="step step-5">
      <span class="step-number">5.</span>
      <span class="step-text">Submit your Corkage Fee<br>Details!</span>
    </div>
  </section>

</main>
</body>
</html>
```